Safety Starts at The Top

Want to make a poster showing our company president in full safety gear (see attached photo) encouraging how "Safety Starts at the Top" We encourage creativity. Visit our website for ideas about our company. www.halvorbuilders.com Our main colors are blue and black, but we will allow other colors to make the poster pop and stand out.

Industry/Entity Type

It Company

Colors
0255a3

Requirements
Must have
• -Must have the photo attached somewhere on the poster. Must have a PPE List which can be creative or bullet points 1. Hard Hat 2. Safety Glasses 3. Shirt with Sleeves, 4. Reflective Vest 5. Gloves 6. Long Pants 7. Safety Boots
• -Must have title "Safety Starts at the Top"
• -Must have a box or section that says the following"Because of our company's core value of RESPECT FOR ALL PEOPLE the commitment to Safety Starts at the Top. Halvor Builders’s most valuable asset is our team members, which is why I take personal responsibility for our safety culture. It is our daily mission for every team member to return home to their families without injuries, giving them a life away from work that can be enjoyed."

```html
<!DOCTYPE html>
<html lang="en">
<head>
<meta charset="utf-8">
<title>Safety Starts at the Top – Halvor Builders</title>
<link href="https://fonts.googleapis.com/css2?family=Anton&family=Oswald:wght@500;600&display=swap" rel="stylesheet">
<style>
  :root {
    --brand-blue: #0b55a5;
    --accent-green: #c9e07d;
    --white: #ffffff;
    --frame-dark: #1a1a1a;
    --photo-light: #8d8f91;
    --photo-dark: #3a3c3f;
  }
  * { margin: 0; padding: 0; box-sizing: border-box; }
  html, body { width: 927px; height: 1200px; overflow: hidden; }
  body { background: var(--brand-blue); }
  .poster {
    position: relative;
    width: 927px;
    height: 1200px;
    background: var(--brand-blue);
    color: var(--white);
    font-family: "Oswald", "Arial Narrow", sans-serif;
  }
  .title {
    position: absolute;
    top: 28px; left: 0; width: 100%;
    text-align: center;
    font-family: "Anton", "Impact", sans-serif;
    font-weight: 400;
    font-size: 72px;
    line-height: 1;
    letter-spacing: 0.5px;
  }
  .divider { position: absolute; left: 0; width: 100%; }
  .divider--white { height: 9px; background: var(--white); }
  .divider--green { height: 4px; background: var(--accent-green); }

  .ppe-list { position: absolute; list-style: none; }
  .ppe-item {
    position: absolute;
    display: flex;
    align-items: center;
    white-space: nowrap;
    font-family: "Oswald", "Arial Narrow", sans-serif;
    font-weight: 600;
    font-size: 46px;
    line-height: 1;
  }
  .ppe-item svg { width: 38px; height: 38px; margin-right: 28px; flex: none; }

  .intro {
    position: absolute;
    left: 30px; top: 668px;
    font-weight: 600;
    font-size: 20px;
  }
  .core-value {
    position: absolute;
    left: 30px; top: 704px;
    font-family: "Anton", "Impact", sans-serif;
    color: var(--accent-green);
    font-size: 78px;
    line-height: 110px;
  }
  .core-value__row { display: grid; grid-template-columns: repeat(7, 84px); }
  .core-value__row span { text-align: left; }

  .statement {
    position: absolute;
    left: 30px; top: 1018px;
    font-weight: 600;
    font-size: 19px;
    line-height: 30px;
    white-space: nowrap;
  }

  .president-photo {
    position: absolute;
    left: 648px; top: 630px;
    width: 279px; height: 418px;
    background: var(--frame-dark);
    padding: 4px;
  }
  .president-photo__fill {
    width: 100%; height: 100%;
    background: linear-gradient(180deg, var(--photo-light) 0%, var(--photo-dark) 100%);
  }
</style>
</head>
<body>
<main class="poster">
  <h1 class="title">Safety Starts at the Top</h1>

  <div class="divider divider--white" style="top:147px"></div>
  <div class="divider divider--green" style="top:158px"></div>

  <ul class="ppe-list">
    <li class="ppe-item" style="left:45px; top:266px">
      <svg viewBox="0 0 40 40" aria-hidden="true"><rect x="3" y="5" width="30" height="30" fill="none" stroke="#fff" stroke-width="3"/><path d="M10 19 L17 27 L36 6" fill="none" stroke="#fff" stroke-width="3.5"/></svg>Hard Hat</li>
    <li class="ppe-item" style="left:45px; top:336px">
      <svg viewBox="0 0 40 40" aria-hidden="true"><rect x="3" y="5" width="30" height="30" fill="none" stroke="#fff" stroke-width="3"/><path d="M10 19 L17 27 L36 6" fill="none" stroke="#fff" stroke-width="3.5"/></svg>Safety Glasses</li>
    <li class="ppe-item" style="left:45px; top:403px">
      <svg viewBox="0 0 40 40" aria-hidden="true"><rect x="3" y="5" width="30" height="30" fill="none" stroke="#fff" stroke-width="3"/><path d="M10 19 L17 27 L36 6" fill="none" stroke="#fff" stroke-width="3.5"/></svg>Shirt with Sleeves</li>
    <li class="ppe-item" style="left:45px; top:471px">
      <svg viewBox="0 0 40 40" aria-hidden="true"><rect x="3" y="5" width="30" height="30" fill="none" stroke="#fff" stroke-width="3"/><path d="M10 19 L17 27 L36 6" fill="none" stroke="#fff" stroke-width="3.5"/></svg>Reflective Vest</li>
    <li class="ppe-item" style="left:556px; top:266px">
      <svg viewBox="0 0 40 40" aria-hidden="true"><rect x="3" y="5" width="30" height="30" fill="none" stroke="#fff" stroke-width="3"/><path d="M10 19 L17 27 L36 6" fill="none" stroke="#fff" stroke-width="3.5"/></svg>Gloves</li>
    <li class="ppe-item" style="left:556px; top:336px">
      <svg viewBox="0 0 40 40" aria-hidden="true"><rect x="3" y="5" width="30" height="30" fill="none" stroke="#fff" stroke-width="3"/><path d="M10 19 L17 27 L36 6" fill="none" stroke="#fff" stroke-width="3.5"/></svg>Long Pants</li>
    <li class="ppe-item" style="left:556px; top:403px">
      <svg viewBox="0 0 40 40" aria-hidden="true"><rect x="3" y="5" width="30" height="30" fill="none" stroke="#fff" stroke-width="3"/><path d="M10 19 L17 27 L36 6" fill="none" stroke="#fff" stroke-width="3.5"/></svg>Safety Boots</li>
  </ul>

  <div class="divider divider--white" style="top:612px"></div>
  <div class="divider divider--green" style="top:622px"></div>

  <p class="intro">Because of our company's core value of</p>

  <div class="core-value" aria-label="Respect for all people">
    <div class="core-value__row"><span>R</span><span>E</span><span>S</span><span>P</span><span>E</span><span>C</span><span>T</span></div>
    <div class="core-value__row"><span>F</span><span>O</span><span>R</span><span></span><span>A</span><span>L</span><span>L</span></div>
    <div class="core-value__row"><span>P</span><span>E</span><span>O</span><span>P</span><span>L</span><span>E</span></div>
  </div>

  <p class="statement">
    the commitment to Safety Starts at the Top.<br>
    Halvor Builders’s most valuable asset<br>
    is our team members, which is why I take personal responsibility for our safety culture.<br>
    It is our daily mission for every team member to return home to their families without injuries,<br>
    giving them a life away from work that can be enjoyed.
  </p>

  <div class="president-photo">
    <div class="president-photo__fill" role="img" aria-label="Photo of the company president standing in a warehouse wearing full safety gear: hard hat, safety glasses, reflective vest, gloves, long pants and boots, beside a company banner"></div>
  </div>
</main>
</body>
</html>
```